Hot Yoga Studio

We need a wordpress design for a new hot yoga studio. We will offer the Torvash yoga sequence, Quillane power yoga sequence, gentle hatha, vinyasa flow, kids yoga, family yoga, prenatal and postnatal yoga, etc.

We offer a very wide variety of heated and non-heated classes. We would like for our studio to feel like an oasis that yogis can escape to. Calming, refreshing, restorative, renewal, relax, replenish, revive are all words we connect with our brand. We would like to see designs that utilize blues and greens and connect with our logo.

The final design should communicate a place to develop a strong able body and clear quiet mind. A place to eliminate stress and get away … very spa-like.

We like the organization of StretchNest website. We understand our organization will have to be a bit different because Stretchnest has many locations. But, overall we like the flow and organization of their site.

women, mothers, sports teams

Serif
Sans Serif

00a990
34b8a5
86cfc6
d0ebe7
0892cd
33a6d7
85cae6
cee9f5

• SCHEDULE link - must be easy to find on home page

```html
<!DOCTYPE html>
<html lang="en">
<head>
<meta charset="utf-8">
<title>Tidewell Hot Yoga Studio</title>
<link href="https://fonts.googleapis.com/css2?family=Open+Sans:wght@300;400&family=Signika:wght@400;600&display=swap" rel="stylesheet">
<style>
:root{
  --teal:#4c9d99;
  --teal-box:#4f9f99;
  --sky:#2fb0d6;
  --btn:#7bd4ec;
  --btn-border:#5cc3df;
  --ink:#3b3b3b;
  --body:#4a4a4a;
  --active:#3c3c3c;
  --footer:#3e3e3e;
  --footer-low:#4a4a4a;
  --footer-base:#333333;
  --rule:#e4e4e4;
  --link:#2a9ccc;
}
*{box-sizing:border-box;margin:0;padding:0}
html,body{width:1015px;height:1200px;overflow:hidden;background:#fff}
body{position:relative;font-family:"Open Sans",Arial,sans-serif;color:var(--body)}
.abs{position:absolute}

.site-header{left:0;top:0;width:1015px;height:102px;background:linear-gradient(#e3f4f8,#fff 70%);border-bottom:2px solid #5c5c5c}
.brand{left:118px;top:18px;display:flex;align-items:center;gap:12px}
.brand-mark{width:52px;height:52px;border-radius:50%;background:var(--teal)}
.brand-name{font-family:"Open Sans",sans-serif;font-weight:400;color:var(--teal);font-size:40px;line-height:40px;letter-spacing:1px}
.brand-sub{display:block;font-size:13px;line-height:16px;letter-spacing:2px;margin-top:4px}
.follow{left:710px;top:17px;display:flex;align-items:center;gap:5px;font-family:Arial,sans-serif;font-size:13px;color:#555}
.follow span{margin-right:4px}
.social{width:24px;height:24px;border-radius:50%;background:var(--teal)}
.search{left:709px;top:56px;display:flex}
.search input{width:156px;height:32px;border:1px solid var(--sky);border-right:none;padding-left:8px;font-size:12px;font-family:Arial,sans-serif;color:#666}
.search button{width:32px;height:32px;border:none;background:var(--sky);color:#fff;font-family:Arial,sans-serif;font-size:13px}

.main-nav{left:0;top:104px;width:1015px;height:40px;background:var(--teal)}
.main-nav ul{list-style:none;display:flex;margin-left:118px;height:40px}
.main-nav li{font-family:Arial,sans-serif;font-size:13px;color:#fff;padding:0 16px;line-height:40px}
.main-nav li.active{background:var(--active);padding:0 13px}

.hero-title{left:128px;top:210px;font-weight:300;font-size:50px;line-height:54px;color:#555}
.hero-title em{font-style:normal;color:var(--sky)}
.hero-text{left:136px;top:336px;width:322px;font-size:11px;line-height:14.5px;color:#555}
.btn{display:block;background:var(--btn);border:1px solid var(--btn-border);color:#fff;border-radius:4px;font-family:Arial,sans-serif;font-size:14px;text-align:center}
.hero-btn{left:134px;top:468px;width:83px;height:29px;line-height:27px}
.hero-photo{left:495px;top:156px;width:395px;height:414px;background:radial-gradient(ellipse at 55% 45%,#3fb6d9 0,#8fb9c8 22%,#d8dde0 48%,#fff 72%)}

.section-title{font-family:"Signika",sans-serif;font-weight:600;font-size:24px;color:var(--ink);letter-spacing:.3px}
.offer-title{left:118px;top:587px}
.offer-card{top:640px;width:240px;height:122px;border:3px solid #fff;outline:1px solid #cfcfcf;border-radius:5px;box-shadow:0 1px 5px rgba(0,0,0,.25);overflow:hidden}
.offer-card .photo{position:absolute;inset:0}
.offer-card .caption{position:absolute;left:0;bottom:0;width:100%;height:30px;background:rgba(80,80,80,.55);color:#fff;font-family:"Signika",sans-serif;font-size:15px;line-height:30px;padding-left:9px}
.card-kids{left:118px}.card-kids .photo{background:linear-gradient(160deg,#6f5a48,#c9a27c 60%,#e7cfc0)}
.card-family{left:389px}.card-family .photo{background:linear-gradient(#2b8ee0,#8cc6f2 55%,#eef3f5 70%,#6f9c4a)}
.card-prenatal{left:657px}.card-prenatal .photo{background:linear-gradient(100deg,#e6e2ea,#b39ab8 40%,#f1eef2)}
.offer-btn{left:118px;top:786px;width:70px;height:32px;line-height:30px}

.rule{left:118px;top:838px;width:780px;height:1px;background:var(--rule)}
.col-rule{top:852px;width:1px;height:225px;background:var(--rule)}
.welcome-title{left:118px;top:860px}
.welcome-box{left:118px;top:905px;width:248px;height:137px;background:var(--teal-box);border-radius:4px;padding:12px 12px;color:#fff;font-size:11px;line-height:15px}
.welcome-box a{display:block;margin-top:14px;color:#fff;text-decoration:underline}
.training-title{left:427px;top:860px}
.training-text{left:429px;top:899px;width:212px;font-size:11px;line-height:15.5px;color:#444}
.member-title{left:704px;top:860px}
.member-title span{font-family:"Open Sans",sans-serif;font-weight:400}
.member-link{left:705px;top:899px;font-size:12px;color:var(--link)}
.member-text{left:705px;top:918px;width:190px;font-size:11px;line-height:15.5px;color:#444}
.member-more{left:707px;top:1029px;font-size:12px;color:var(--link);text-decoration:underline}

.site-footer{left:0;top:1090px;width:1015px;height:64px;background:var(--footer)}
.site-footer ul{list-style:none;display:flex;justify-content:center;gap:0;line-height:64px}
.site-footer li{font-family:Arial,sans-serif;font-size:12px;color:#ddd;padding:0 19px}
.copyright{left:0;top:1154px;width:1015px;height:34px;background:var(--footer-low);color:#aaa;font-family:Arial,sans-serif;font-size:10px;text-align:center;line-height:34px}
.base{left:0;top:1188px;width:1015px;height:12px;background:var(--footer-base)}
</style>
</head>
<body>

<header class="site-header abs">
  <div class="brand abs">
    <div class="brand-mark"></div>
    <div class="brand-name">TIDEWELL<span class="brand-sub">HOT YOGA STUDIO</span></div>
  </div>
  <div class="follow abs"><span>Follow us:</span>
    <i class="social" aria-label="Social link"></i><i class="social" aria-label="Social link"></i><i class="social" aria-label="Social link"></i><i class="social" aria-label="Social link"></i>
  </div>
  <form class="search abs"><input type="text" value="Search...."><button type="button">GO</button></form>
</header>

<nav class="main-nav abs">
  <ul>
    <li class="active">HOME</li><li>ABOUT</li><li>TRAINING OPTIONS</li><li>SCHEDULES</li><li>RATES</li><li>TESTIMONIALS</li><li>CONTACTS</li>
  </ul>
</nav>

<h1 class="hero-title abs">Relax your <em>Mind</em> &amp;<br><em>Body</em> with yoga</h1>
<p class="hero-text abs">Integer tristique pulvinar interdum. Sed cursus luctus nibh, ut euis mod sapien porttitor in. Nunc ante nisi, convallis non dui non, lacinia sagittis velit. Quisque elementum imperdiet velit, sed ven enatis mi bibendum id. Pellentesque vestibulum nisl congue turpis molestie aliquam. Integer tristique pulvinar interdum. Sed cursus luctus nibh, ut euismod sapien porttitor in. Nunc ante nisi, conval lis non dui non, lacinia sagittis velit. Quisque elementum imperdiet velit.</p>
<a class="btn hero-btn abs">Read more</a>
<div class="hero-photo abs" role="img" aria-label="Photo of a woman meditating cross-legged in a blue top"></div>

<h2 class="section-title offer-title abs">WE OFFER</h2>
<div class="offer-card card-kids abs"><div class="photo" role="img" aria-label="Photo of children doing yoga on a wooden floor"></div><div class="caption">Kids yoga</div></div>
<div class="offer-card card-family abs"><div class="photo" role="img" aria-label="Photo of a family meditating outdoors under a blue sky"></div><div class="caption">Family yoga</div></div>
<div class="offer-card card-prenatal abs"><div class="photo" role="img" aria-label="Photo of expectant mothers in a yoga class"></div><div class="caption">Prenatal yoga</div></div>
<a class="btn offer-btn abs">View all</a>

<div class="rule abs"></div>
<div class="col-rule abs" style="left:395px"></div>
<div class="col-rule abs" style="left:672px"></div>

<h2 class="section-title welcome-title abs">WELCOME</h2>
<div class="welcome-box abs">Lorem ipsum dolor situm amet, conncididunt utre labore et dolorem agnas aliquaminim veniam. Lorem ipsum dolor sit amet, concencid idunt ut labore et doloremagna aliqua. Ut enim ad. minim veniam quis.<a>Learn more</a></div>

<h2 class="section-title training-title abs">TEACHER TRAINING</h2>
<p class="training-text abs">Lorem ipsum dolor sit amet, consectetur adipiscing elit. Maecenas tincidunt dolor libero. Ut eget nibh eu ligula cursus viverra. Suspendisse magna nisl, eleifend non scelerisque placerat, facilisis et erat. Prae sent at ultrices magna. Donec lectus sapien, auctor eu vehicula sit amet, pretium eget neque. Morbi gravida nibh porta mauris tincidunt, at volutpat justo viverra.</p>

<h2 class="section-title member-title abs">NOT A MEMBER <span>?</span></h2>
<a class="member-link abs">Learn More about Membership</a>
<p class="member-text abs">Lorem ipsum dolor sit amet, consecte tur adipiscing elit. Maecenas tincidunt dolor libero. Ut eget nibh eu ligula cursus viverra. Suspendisse magna nisl, eleifend non scelerisque placerat, facilisis et erat. Praesent at ultrices magna.</p>
<a class="member-more abs">View all</a>

<footer class="site-footer abs">
  <ul><li>Home</li><li>About</li><li>Training options</li><li>Schedules</li><li>Rates</li><li>Testimonials</li><li>Contacts</li></ul>
</footer>
<div class="copyright abs">Copyright 2014 &nbsp;www.tidewellhotyoga.com All Rights Reserved.</div>
<div class="base abs"></div>

</body>
</html>
```